Luxury sell sheet flyer Design

We need two luxury/premium looking sales flyer - one for luxury and one for travel-

Please find flyers from last year (2015) attached. Please copy the pictures and the look and feel (and colors), and use the content form the 2016 documents.

These flyers will be used for corporate subscription sales and targetted at CMOs and Market Pulse heads. As such they should convey a very premium look and feel.

Please provide in format that we can make text edits in later.

Target Market(s)

USA, UK, Asia

Industry/Entity Type

Travel

Font styles to use
Serif

Requirements
Must have
• Good copyright free pictures, no clip art, that show a very premium look and feel for a corporate flyer
Nice to have
• clean feel, not cluttered
Should not have
• clip art

```html
<!DOCTYPE html>
<html lang="en">
<head>
<meta charset="utf-8">
<title>Affluent Asian Travel Consumer Reports</title>
<link href="https://fonts.googleapis.com/css2?family=Tinos:ital,wght@0,400;0,700;1,400;1,700&family=Arimo:wght@700&display=swap" rel="stylesheet">
<style>
:root{
  --ink:#111;
  --sky-top:#7cc3ee;
  --sky-mid:#cfe8f8;
  --sky-light:#f2f8fc;
  --rule:#4a97d0;
  --cell:#ffffff;
  --band:#d9c4a8;
  --divider:#8a8a8a;
}
*{margin:0;padding:0;box-sizing:border-box}
html,body{width:927px;height:1200px;overflow:hidden}
body{font-family:"Tinos","Times New Roman",serif;color:var(--ink);position:relative}
.backdrop{position:absolute;inset:0;
  background:
   radial-gradient(ellipse 420px 260px at 450px 360px,rgba(255,255,255,.85),rgba(255,255,255,0) 70%),
   radial-gradient(ellipse 500px 300px at 800px 60px,rgba(255,255,255,.7),rgba(255,255,255,0) 70%),
   radial-gradient(ellipse 520px 320px at 120px 900px,rgba(255,255,255,.75),rgba(255,255,255,0) 70%),
   radial-gradient(ellipse 360px 260px at 900px 700px,rgba(255,255,255,.8),rgba(255,255,255,0) 70%),
   linear-gradient(160deg,var(--sky-top) 0%,var(--sky-mid) 45%,var(--sky-light) 70%,var(--sky-mid) 100%)}
.base-band{position:absolute;left:0;right:0;top:1183px;height:17px;background:var(--band)}
.abs{position:absolute}
.title{left:41px;top:22px;font-size:20.5px;font-weight:700;letter-spacing:.3px}
.subtitle{left:41px;top:49px;font-size:14.3px}
.cat-head{left:41px;top:80px;font-size:14.3px;font-weight:700;font-style:italic}
table{border-collapse:collapse}
.categories{left:41px;top:100px;width:757px;background:var(--cell)}
.categories td{border:1px solid var(--rule);height:25px;padding:0 0 0 17px;font-size:14.3px;white-space:nowrap}
.intro{left:41px;top:189px;width:480px;font-size:14.6px;line-height:18px}
.markets{left:41px;top:306px;width:480px;font-size:14.6px;line-height:18px}
.markets b{font-size:14.6px}
.markets .extra{margin-top:7px}
.def-head{left:547px;top:193px;font-size:14.3px}
.def-table{left:541px;top:219px;width:261px;font-size:12px;font-weight:700}
.def-table th{text-align:left;font-size:12px;height:22px;padding-left:14px}
.def-table th+th{padding-left:30px}
.def-table td{background:var(--cell);border:1px solid var(--rule);height:25.6px;padding-left:14px}
.def-table td+td{font-weight:400;padding-left:30px;font-size:12.4px}
.divider{left:41px;top:470px;width:815px;height:1px;background:var(--divider)}
.col{font-size:11.5px;line-height:15.2px}
.col p{margin-bottom:6px}
.col-left{left:41px;top:488px;width:378px}
.col-right{left:442px;top:484px;width:414px}
.topics{display:flex;margin-top:-2px}
.topics ul{list-style:none}
.topics .a{width:180px}
.topics .b{width:200px;padding-top:0}
.topics .a li.sub{padding-left:14px}
.topics .b li{padding-left:18px;position:relative}
.topics .b li::before{content:"•";position:absolute;left:2px}
.tier{font-weight:700}
.tier-item{padding-left:16px}
.featured{left:117px;top:1078px;font-family:"Arimo",Arial,sans-serif;font-weight:700;font-size:15px;line-height:20px;color:#222}
.press{left:425px;top:1061px;width:451px;height:111px;background:#f7f7f7;display:flex;flex-direction:column;justify-content:space-around;padding:8px 8px;font-size:11px;font-weight:700;color:#222}
.press .row{display:flex;justify-content:space-around;align-items:center}
</style>
</head>
<body>
<div class="backdrop" role="img" aria-label="Soft blue sky with light white clouds"></div>
<div class="base-band"></div>

<h1 class="abs title">AFFLUENT ASIAN TRAVEL CONSUMER REPORTS</h1>
<p class="abs subtitle">The 2016 subscription includes two reports per market, one released half-way and the other one at the end of the year.</p>
<p class="abs cat-head">The following travel and luxury product categories are covered in each market:</p>

<table class="abs categories">
<tr><td>Hotels (49 brands)</td><td>Cruise Lines (21 brands)</td><td>Airlines (50 brands)</td></tr>
<tr><td>Travel Destinations (44 destinations</td><td>Designer Clothing &amp; Accessories (83 brands)</td><td>Watches (82 brands)</td></tr>
<tr><td>Jewellery (39 brands)</td><td>Skincare (52 brands)</td><td>Makeup (49 brands)</td></tr>
</table>

<p class="abs intro">In each market we are focusing on affluent travel consumers (approximately top-20% of the population based on household income) who have travelled internationally in the past 12 months or planning to travel in the next 12 months. We are fielding two waves in 2016, and interviewing a total of n=300 affluent consumers in each market (at least 100 respondents in each market are past-12/next-12-month cruise travellers/intenders).</p>

<div class="abs markets">
<p>Markets included in the study (content is partially trended to last year in all markets)</p>
<p><b>• China • India • Singapore &nbsp;• Hong Kong &nbsp;• Malaysia &nbsp;• S. Korea<br>• Taiwan &nbsp;• Japan</b></p>
<p class="extra">Other markets, such as, Indonesia, Thailand, and Australia can be added by request.</p>
</div>

<p class="abs def-head">Affluent consumer definitions are as follows:</p>
<table class="abs def-table">
<tr><th>COUNTRY</th><th>Annual HHI</th></tr>
<tr><td>China</td><td>CNY 200,000+</td></tr>
<tr><td>India</td><td>INR 12,00,000+</td></tr>
<tr><td>Singapore</td><td>SGD 110,000+</td></tr>
<tr><td>Hong Kong</td><td>HKD 720,000+</td></tr>
<tr><td>Malaysia</td><td>MYR 120,000+</td></tr>
<tr><td>South Korea</td><td>KRW 78 million +</td></tr>
<tr><td>Taiwan</td><td>NT$ 960,000+</td></tr>
<tr><td>Japan</td><td>JPY 10,000,000+</td></tr>
</table>

<div class="abs divider"></div>

<div class="abs col col-left">
<p><b>Key analytics in the reports include:</b><br><b>Luxury Brand Index</b> – A tool to help brands understand how well they are meeting the expectation of their potential travel customers in relation to their competitors in different markets. The index is derived from the importance of different dimensions of luxury on category purchase intent and brands' ratings on the same dimensions.</p>
<p><b>Luxury Brand Media Reach</b> – Gives the brands vital information on how well they are being noticed by travellers in the most relevant media touchpoints. This is calculated based on the importance of different media touchpoints for affecting category purchasing and recall of brand recall in the relevant touchpoints.</p>
<p><b>Luxury Consumer Segmentation</b> - We have identified unique key luxury consumer types that are different in their motivations and purchase behaviour towards luxury brands. This segmentation will help brands understand their key consumer types in each market.</p>
<p><b>Affluent Luxury Consumer Insights</b> – We will have numerous analyses to help you understand and profile affluent Asian travel consumers in each market, looking at their purchase behaviour, media influences, psychographics, and demographics. Many of the analyses will be trended to understand shifts in consumer preferences. Key topics for the analyses include:</p>
<div class="topics">
<ul class="a">
<li>• Purchase Triggers</li><li>• Most recent trip</li>
<li class="sub">Influences</li><li class="sub">Loyalty programs</li><li class="sub">Advertising</li><li class="sub">Recommendations</li><li class="sub">Editorials</li><li class="sub">Travel agents</li><li class="sub">How travel was booked</li><li class="sub">Class of travel</li><li class="sub">Destination type</li><li class="sub">Activities</li>
</ul>
<ul class="b">
<li>What looking forward to from next trip?</li><li>Travel and Luxury Categories and Brands Intended to Purchase</li><li>Spend and Share of Wallet for Different Luxury Categories</li><li>Media Touchpoints Relevant to Each Category</li><li>Psychographics around Luxury Travel Purchase Behaviour</li><li>Hobbies and Interests</li><li>Travel preferences</li><li>Affluent Travel Consumer Profiles</li>
</ul>
</div>
</div>

<div class="abs col col-right">
<p><b>SEMI-ANNUAL ROUNDTABLES</b> (with Senior Executives from the Luxury Travel World)<br>These are private, invitation-only, informal lunch and evening sessions held quarterly at central premium locations in Hong Kong and Singapore. During these sessions we will share latest findings on affluent Asian travel consumers and moderate a discussion on topical themes among travel leaders (including executives from luxury travel brands and travel though leaders).</p>
<p><b>CUSTOM TABULATIONS OF DATA</b><br>We will provide a set of tabulations of the data for all basic graphs included in the report with custom cuts (up to 20 banner points), e.g., you target consumer age groups, or consumers who are planning a purchase from your competitive brand set.</p>
<p style="margin-top:10px"><b>SEMI-ANNUAL BRAINSTORMING SESSIONS</b> (with Halcyon Experts)<br>We will facilitate two brainstorming sessions (timed after the release of each of the Affluent Consumer and Luxury Brand Reports). In these two-hour sessions we walk you through the findings from the latest data release, and together with you look at implications the findings have on your specific brand(s), and brainstorm on how your brand can best make us of the findings. These sessions can be held in our or your premises in Singapore or Hong Kong.<br>2016 Affluent Insights Travel Subscription Service has three optional service tiers:</p>
<div>
<div class="tier">Affluent Insights Plus</div>
<div class="tier-item">2 Affluent Asian Travel Consumer Reports</div>
<div class="tier">Affluent Insights Premium</div>
<div class="tier-item">2 Affluent Asian Travel Consumer Reports</div>
<div class="tier-item">1 Invitation to Semi-annual Travel Leader Roundtables</div>
<div class="tier-item">1 Set of Custom Tabulations of Data (per market)</div>
<div class="tier">Affluent Insights Prestige</div>
<div class="tier-item">2 Affluent Asian Travel Consumer Reports</div>
<div class="tier-item">2 Invitations to Semi-annual Travel Leader Roundtables</div>
<div class="tier-item">2 Sets of Custom Tabulations of Data (per market)</div>
<div class="tier-item">2 Semi-annual Brainstorming Sessions (per market) or speaking engagements. (We have spoken at key events with World Luxury Travel Forum, Gilded Review, Voyage Insight, Global Daily Herald (Travel &amp; Luxury Summit), and Prestige Circle)</div>
<div class="tier-item">Pricing for each category is as follows:</div>
</div>
</div>

<p class="abs featured">Our research has been featured<br>in international media, such as:</p>
<div class="abs press">
<div class="row"><span>Gilded Review</span><span>Global Daily Herald</span><span>Northwave News</span><span>Market Pulse</span><span>AsiaLink</span><span>TechHarbor</span></div>
<div class="row"><span>Straitcast</span><span>Lorgnette</span><span>Brandline</span><span>Commerce Times</span><span>Prestige Circle</span><span>Eastern Daily</span></div>
<div class="row" style="justify-content:center;gap:26px"><span>Chao Phraya Post</span><span>LedgerWire</span><span>MarketsTV</span></div>
</div>
</body>
</html>
```